New Business Card Design Project

We are looking for a talented individual to create a truly awesome/unique business card design for us. We are looking for a someone to design something that will really stand out from the crowd - we don't mind what ideas you come up with (ie embossed/flat/matte/shine etc etc) just wow us with your creativity.
Updates

Sick

Target Market(s)

Video Games Industry Professionals (all levels of seniority from QA Testers through to CEOs)

Contact Information for Business Card

Company logo (see upload)
Company name: Northbridge Play Careers Ltd
Employee Name: Harriet Vasko
Job title: CEO
Website: www.npc2go.com
Office +44 1632 960418
Mobile: +44 7700 900582
Email: harriet@npc2go.com

Colors

Designer to choose colors to be used in the design.

Requirements
Must have
• The business card design MUST contain all the information listed in the BUSINESS CARD DETAILS box.
• You will see the colours that are relevant to us (ie company logo) in the uploaded imagery - however you do not have to use all these colours when designing the business card itself
• MUST BE DOUBLE SIDED

```html
<!DOCTYPE html>
<html lang="en">
<head>
<meta charset="utf-8">
<title>Northbridge Play Careers – Business Card</title>
<link href="https://fonts.googleapis.com/css2?family=Lato:wght@400;700&display=swap" rel="stylesheet">
<style>
  :root {
    --navy: #2e3660;
    --navy-deep: #262d52;
    --orange: #f07a1e;
    --white: #ffffff;
    --ink: #1f2547;
    --ghost: #eef0f3;
    --stage: #e4e5e8;
  }
  * { margin: 0; padding: 0; box-sizing: border-box; }
  html, body { width: 1200px; height: 800px; overflow: hidden; }
  body {
    background: var(--stage);
    font-family: "Lato", Arial, sans-serif;
    display: flex;
    flex-direction: column;
    align-items: center;
    justify-content: center;
    gap: 40px;
  }
  .card {
    position: relative;
    width: 600px;
    height: 343px;
    border-radius: 3px;
    overflow: hidden;
    box-shadow: 0 6px 18px rgba(0,0,0,0.18);
  }

  /* Front side */
  .card--front { background: var(--navy); color: var(--white); }
  .card--front .brand {
    position: absolute;
    left: 0; right: 0; top: 120px;
    display: flex; align-items: center; justify-content: center; gap: 16px;
  }
  .brand__dot {
    width: 54px; height: 54px; border-radius: 50%;
    background: var(--white);
    flex: none;
  }
  .brand__name {
    font-weight: 700;
    font-size: 30px;
    letter-spacing: 0.5px;
    line-height: 1;
  }
  .card--front .brand__name { color: var(--white); }
  .card--front .site {
    position: absolute; left: 0; right: 0; bottom: 44px;
    text-align: center;
    font-size: 14px; letter-spacing: 1.2px;
  }

  /* Back side */
  .card--back { background: var(--white); color: var(--ink); }
  .card--back::after {
    content: ""; position: absolute; left: 0; right: 0; bottom: 0;
    height: 8px; background: var(--navy);
  }
  .ghost-mark {
    position: absolute; right: -40px; top: 10px;
    width: 300px; height: 300px; border-radius: 50%;
    background: var(--ghost);
  }
  .card--back .brand {
    position: absolute; left: 36px; top: 44px;
    display: flex; align-items: center; gap: 14px;
  }
  .card--back .brand__dot { background: var(--navy); width: 48px; height: 48px; }
  .card--back .brand__name { color: var(--navy); font-size: 24px; }
  .person {
    position: absolute; left: 400px; top: 150px;
  }
  .person__name { font-size: 22px; font-weight: 700; color: var(--ink); }
  .person__role { font-size: 14px; margin-top: 4px; padding-left: 8px; }
  .company {
    position: absolute; left: 36px; top: 196px;
    font-size: 15px; font-weight: 700; color: var(--navy);
  }
  .contacts {
    position: absolute; left: 36px; top: 228px;
    list-style: none;
    font-size: 15px; line-height: 21px;
  }
  .contacts li { display: flex; align-items: center; gap: 12px; }
  .contacts svg { width: 13px; height: 13px; fill: var(--ink); flex: none; }
</style>
</head>
<body>

  <section class="card card--front" aria-label="Card front">
    <div class="brand">
      <span class="brand__dot"></span>
      <span class="brand__name">Northbridge Play Careers</span>
    </div>
    <p class="site">www.npc2go.com</p>
  </section>

  <section class="card card--back" aria-label="Card back">
    <div class="ghost-mark" aria-hidden="true"></div>
    <div class="brand">
      <span class="brand__dot"></span>
      <span class="brand__name">Northbridge Play Careers</span>
    </div>
    <div class="person">
      <p class="person__name">Harriet Vasko</p>
      <p class="person__role">CEO</p>
    </div>
    <p class="company">Northbridge Play Careers Ltd</p>
    <ul class="contacts">
      <li>
        <svg viewBox="0 0 16 16"><path d="M3 1l3 3-1.5 2c1 2 3 4 5 5l2-1.5 3 3-2 2C7 14 2 9 1 3z"/></svg>
        +44 1632 960418
      </li>
      <li>
        <svg viewBox="0 0 16 16"><path d="M4 0h8v16H4zM5.5 2v10h5V2zM7 13h2v2H7z"/></svg>
        +44 7700 900582
      </li>
      <li>
        <svg viewBox="0 0 16 16"><path d="M0 3h16v10H0zM1.5 4.5L8 9l6.5-4.5V12h-13z"/></svg>
        harriet@npc2go.com
      </li>
      <li>
        <svg viewBox="0 0 16 16"><path d="M8 0a8 8 0 100 16A8 8 0 008 0zm0 1.5c1 1 1.8 3 2 5.7H6C6.2 4.5 7 2.5 8 1.5zM1.6 7.2a6.5 6.5 0 013-5C4 3.8 3.6 5.5 3.5 7.2zm0 1.6h1.9c.1 1.7.5 3.4 1.1 5a6.5 6.5 0 01-3-5zm4.4 0h4c-.2 2.7-1 4.7-2 5.7-1-1-1.8-3-2-5.7zm6.5 0h1.9a6.5 6.5 0 01-3 5c.6-1.6 1-3.3 1.1-5zm0-1.6c-.1-1.7-.5-3.4-1.1-5a6.5 6.5 0 013 5z"/></svg>
        www.npc2go.com
      </li>
    </ul>
  </section>

</body>
</html>
```